Business card design for an industrial flooring company

Designing a eco-friendly/go green/organic looking business card for a concrete Polishing / epoxy coatings company. I am looking for an ecofriendly / organic / go green feel for an industrial flooring company. I need a logo bad. We go out of are way to protect the area where we are working. Filter the air, dispose of the contaminated water, use low VOC products etc. We travel nationwide doing concrete polishing and epoxy coatings for big box stores like Halvane Pondery FurNook penny central. When someone googles environmentally friendly flooring solutions I want them to call me I’m really easy looking for something clean and professional.

Target Market(s)

We target industrial facilities managers all the way to small business owner. Anyone that has a concrete floor. Warehouses, retail space, shops, etc.

Industry/Entity Type

Construction Company

Contact Information for Business Card

Business name- Terra-Gleam, office 555-310-4829, cell 555-847-1906, email dwight@terra-gleam-example.com. No Address

Font styles to use
Serif
Sans Serif
Other font styles liked:
• Arial

Colors
3176b5
85acd3
cfdfed
cedeed
00a990
33b8a4

Requirements
Must have
• Environmentally friendly concrete polishing systems
• Services: Polished concrete, epoxy coatings, overlays, safety striping, staining and dyed concrete, concrete sealing
• a eco-friendly/go green/organic look
Nice to have
• I am looking for an ecofriendly / organic / go green feel for an industrial flooring company. I need a logo bad. We go out of are way to protect the area where we are working. Filter the air, dispose of the contaminated water, use low VOC products.
Should not have
• Shouldn’t be childish unprofessional
• I do not like the logo I attached.

```html
<!DOCTYPE html>
<html lang="en">
<head>
<meta charset="utf-8">
<title>Terra-Gleam Business Card</title>
<link href="https://fonts.googleapis.com/css2?family=Arimo:wght@400&display=swap" rel="stylesheet">
<style>
  :root {
    --page-bg: #2b2d31;
    --card-white: #ffffff;
    --brand-green: #1fa37f;
    --blue-deep: #1a4f9c;
    --blue-mid: #2566b5;
    --sky-pale: #e6eff7;
    --leaf-green: #8cc09a;
    --hill-teal: #5c9a94;
    --text-light: #ffffff;
  }
  * { box-sizing: border-box; margin: 0; padding: 0; }
  html, body {
    width: 1200px; height: 900px; overflow: hidden;
    background: var(--page-bg);
    font-family: "Arimo", Arial, sans-serif;
  }
  .sheet {
    width: 1200px; height: 900px;
    display: flex; flex-direction: column; align-items: center; justify-content: center;
    gap: 40px;
  }
  .card {
    position: relative;
    width: 665px; height: 380px;
    overflow: hidden;
    box-shadow: 0 10px 30px rgba(0,0,0,0.35);
  }
  .brand-name { font-weight: 400; letter-spacing: 1px; }

  /* Front */
  .card-front { background: var(--card-white); }
  .card-front .brand-name {
    position: absolute; left: 0; right: 0; top: 96px;
    text-align: center;
    font-size: 40px; color: var(--brand-green);
  }
  .card-front .landscape {
    position: absolute; left: 0; right: 0; bottom: 0; height: 190px;
    background: linear-gradient(180deg, rgba(255,255,255,0) 0%, var(--sky-pale) 35%, var(--leaf-green) 75%, var(--hill-teal) 100%);
  }

  /* Back */
  .card-back {
    background: linear-gradient(135deg, var(--blue-mid) 0%, var(--blue-deep) 100%);
    color: var(--text-light);
  }
  .card-back .faint-scene {
    position: absolute; left: 0; right: 0; bottom: 0; height: 240px;
    background: linear-gradient(180deg, rgba(133,172,211,0) 0%, rgba(133,172,211,0.16) 60%, rgba(133,172,211,0.08) 100%);
  }
  .card-back .brand-name {
    position: absolute; left: 70px; top: 205px;
    font-size: 42px;
  }
  .card-back .divider {
    position: absolute; left: 368px; top: 110px;
    width: 1px; height: 100px;
    background: rgba(255,255,255,0.55);
  }
  .contact-list {
    position: absolute; left: 400px; top: 118px;
    list-style: none;
    font-size: 14px; line-height: 28px;
  }
  .contact-list .label { display: inline-block; width: 26px; }
</style>
</head>
<body>
  <main class="sheet">
    <section class="card card-front">
      <div class="landscape" role="img" aria-label="Illustrated green landscape with trees, hills, wind turbines, a small factory and a rising sun"></div>
      <h1 class="brand-name">Terra-Gleam</h1>
    </section>

    <section class="card card-back">
      <div class="faint-scene" role="img" aria-label="Faint tone-on-tone landscape of trees and buildings"></div>
      <h2 class="brand-name">Terra-Gleam</h2>
      <div class="divider"></div>
      <ul class="contact-list">
        <li><span class="label">O :</span>555-310-4829</li>
        <li><span class="label">M :</span>555-847-1906</li>
        <li><span class="label">E :</span>dwight@terra-gleam-example.com</li>
      </ul>
    </section>
  </main>
</body>
</html>
```